Pop-up Banner

Would like a design for a pop-up 85 x 206cm banner for a trade show. (from nordel press)
We would like "our logo" (copperline ventures) - then the tagline - "Your Trusted Partner in Data-Driven Decisions"
*Supporting Bullets*
Unified data, analytics & AI
Trusted insights, faster outcomes
Real-time intelligence at scale
Enterprise-ready, secure solutions
Clarity from data complexity
trusted by...some company logos
Partners with : partner logo
Our Colours: #FFA300, #3D4176, #FDD16E, #F87C57, #A68118, #1C2F36

```html
<!DOCTYPE html>
<html lang="en">
<head>
<meta charset="utf-8">
<title>Copperline Ventures – Pop-up Banner Concepts</title>
<link href="https://fonts.googleapis.com/css2?family=Montserrat:wght@700;800&family=Barlow+Semi+Condensed:wght@500;600;700&display=swap" rel="stylesheet">
<style>
  :root{
    --navy:#3D4176;
    --orange:#FFA300;
    --sand:#FDD16E;
    --coral:#F87C57;
    --bronze:#A68118;
    --ink:#1C2F36;
    --paper:#F7F8FA;
    --backdrop:#EAEAEA;
    --partner-grey:#5E6470;
    --partner-green:#2E9C55;
    --trust-teal:#1B8A7A;
    --trust-blue:#2A8BC9;
    --trust-red:#D2334A;
  }
  *{box-sizing:border-box;margin:0;padding:0}
  html,body{width:1200px;height:497px;overflow:hidden}
  body{background:var(--backdrop);position:relative;font-family:"Barlow Semi Condensed",Arial,sans-serif}

  .banner{position:absolute;top:24px;width:174px;height:445px;background:var(--paper);overflow:hidden;box-shadow:0 1px 3px rgba(0,0,0,.12)}
  .banner--classic{left:86px}
  .banner--band{left:506px}
  .banner--fade{left:931px;background:linear-gradient(to bottom,var(--navy) 0,var(--navy) 60px,var(--paper) 100px,var(--paper) 390px,var(--navy) 420px)}

  .banner__header{position:absolute;left:0;top:0;width:100%;height:97px;background:var(--navy)}
  .banner__band{position:absolute;left:0;top:109px;width:100%;height:115px;background:linear-gradient(to bottom,var(--navy) 0,var(--navy) 62%,var(--paper) 100%)}

  .brand{position:absolute;left:0;width:100%;display:flex;justify-content:center;align-items:center;gap:7px}
  .brand__mark{width:30px;height:30px;border-radius:50%;background:var(--orange)}
  .brand__name{font-family:"Montserrat",Arial,sans-serif;font-weight:700;font-size:11px;line-height:13px;color:#fff;letter-spacing:.2px}
  .banner--band .brand__name{color:var(--navy)}
  .banner--band .brand__mark{background:var(--navy)}

  .tagline{position:absolute;left:0;width:100%;text-align:center;font-family:"Montserrat",Arial,sans-serif;font-weight:800;font-size:7px;line-height:10px;letter-spacing:1.4px;color:var(--orange)}
  .banner--band .tagline,.banner--fade .tagline{font-size:7.6px;line-height:12px}

  .benefits{position:absolute;left:0;width:100%;list-style:none;text-align:center;color:var(--navy);font-weight:600;font-size:7.4px;text-transform:uppercase}
  .benefits li{height:18.6px;line-height:18.6px}
  .benefits li::before{content:"• "}
  .banner--band .benefits{color:#fff;font-weight:500;font-size:6.8px}
  .banner--band .benefits li{height:15.3px;line-height:15.3px}

  .section-title{position:absolute;left:0;width:100%;text-align:center;font-family:"Montserrat",Arial,sans-serif;font-weight:800;font-size:7.6px;letter-spacing:1.6px;color:var(--ink)}
  .banner--band .section-title{font-family:"Barlow Semi Condensed",Arial,sans-serif;font-weight:600;letter-spacing:0;font-size:7.6px;color:var(--navy)}
  .banner--fade .section-title{display:flex;align-items:center;justify-content:center;gap:5px;color:var(--orange);font-size:6.4px}
  .banner--fade .section-title::before,.banner--fade .section-title::after{content:"";width:34px;height:1px;background:var(--navy)}

  .logo-row{position:absolute;left:0;width:100%;display:flex;justify-content:center;align-items:center;gap:14px;font-weight:600;font-size:10px;line-height:14px}
  .logo{display:flex;align-items:center;gap:3px;white-space:nowrap}
  .logo__dot{width:9px;height:9px;border-radius:50%}
  .logo__square{width:9px;height:9px}
  .logo--halvern{color:var(--partner-grey)}
  .logo--halvern .logo__square{background:var(--partner-grey)}
  .logo--tarnix{color:var(--trust-red);letter-spacing:.6px}
  .logo--quillsoft{color:var(--partner-green)}
  .logo--quillsoft .logo__dot{background:var(--partner-green)}
  .logo--meridex{color:var(--ink)}
  .logo--lumera{color:var(--ink);letter-spacing:1.4px}
  .logo--veroa{color:var(--trust-teal)}
  .logo--veroa .logo__dot{background:var(--trust-teal)}
  .logo--fenwick{color:var(--partner-grey)}
  .logo--harbour{color:var(--ink);font-size:6px;line-height:7px;font-weight:700;text-transform:uppercase}
  .logo--harbour .logo__square{width:14px;height:14px;background:var(--trust-red)}
  .logo--alder{color:var(--trust-blue)}
  .logo--alder .logo__dot{width:11px;height:11px;background:var(--trust-blue)}

  /* classic */
  .banner--classic .brand{top:28px}
  .banner--classic .tagline{top:71px}
  .banner--classic .benefits{top:122px}
  .banner--classic .title-partners{top:228px}
  .banner--classic .row-p1{top:252px}
  .banner--classic .row-p2{top:280px}
  .banner--classic .title-trusted{top:328px}
  .banner--classic .row-t1{top:352px}
  .banner--classic .row-t2{top:384px}
  /* band */
  .banner--band .brand{top:32px}
  .banner--band .tagline{top:79px}
  .banner--band .benefits{top:122px}
  .banner--band .title-partners{top:224px}
  .banner--band .row-p1{top:248px}
  .banner--band .row-p2{top:280px}
  .banner--band .title-trusted{top:316px}
  .banner--band .row-t1{top:340px}
  .banner--band .row-t2{top:375px}
  /* fade */
  .banner--fade .brand{top:33px}
  .banner--fade .tagline{top:94px}
  .banner--fade .benefits{top:122px}
  .banner--fade .title-partners{top:235px}
  .banner--fade .row-p1{top:258px}
  .banner--fade .row-p2{top:290px}
  .banner--fade .title-trusted{top:327px}
  .banner--fade .row-t1{top:350px}
  .banner--fade .row-t2{top:386px}
</style>
</head>
<body>

<section class="banner banner--classic">
  <div class="banner__header"></div>
  <div class="brand"><span class="brand__mark"></span><span class="brand__name">COPPERLINE<br>VENTURES</span></div>
  <p class="tagline">YOUR TRUSTED PARTNER<br>IN DATA-DRIVEN DECISIONS</p>
  <ul class="benefits">
    <li>Unified data, analytics &amp; AI</li>
    <li>Trusted insights, faster outcomes</li>
    <li>Real-time intelligence at scale</li>
    <li>Enterprise-ready, secure solutions</li>
    <li>Clarity from data complexity</li>
  </ul>
  <h3 class="section-title title-partners">PARTNER WITH</h3>
  <div class="logo-row row-p1"><span class="logo logo--halvern"><span class="logo__square"></span>Halvern</span><span class="logo logo--tarnix">TARNIX</span></div>
  <div class="logo-row row-p2"><span class="logo logo--quillsoft"><span class="logo__dot"></span>quillsoft</span><span class="logo logo--meridex">meridex</span></div>
  <h3 class="section-title title-trusted">TRUSTED BY</h3>
  <div class="logo-row row-t1"><span class="logo logo--lumera">LUMERA</span><span class="logo logo--veroa"><span class="logo__dot"></span>VEROA</span><span class="logo logo--fenwick">Fenwick</span></div>
  <div class="logo-row row-t2"><span class="logo logo--harbour"><span class="logo__square"></span>Harbourgate<br>Port</span><span class="logo logo--alder"><span class="logo__dot"></span>ALDER</span></div>
</section>

<section class="banner banner--band">
  <div class="banner__band"></div>
  <div class="brand"><span class="brand__mark"></span><span class="brand__name">COPPERLINE<br>VENTURES</span></div>
  <p class="tagline">YOUR TRUSTED PARTNER<br>IN DATA-DRIVEN DECISIONS</p>
  <ul class="benefits">
    <li>Unified data, analytics &amp; AI</li>
    <li>Trusted insights, faster outcomes</li>
    <li>Real-time intelligence at scale</li>
    <li>Enterprise-ready, secure solutions</li>
    <li>Clarity from data complexity</li>
  </ul>
  <h3 class="section-title title-partners">PARTNER WITH</h3>
  <div class="logo-row row-p1"><span class="logo logo--halvern"><span class="logo__square"></span>Halvern</span><span class="logo logo--tarnix">TARNIX</span></div>
  <div class="logo-row row-p2"><span class="logo logo--quillsoft"><span class="logo__dot"></span>quillsoft</span><span class="logo logo--meridex">meridex</span></div>
  <h3 class="section-title title-trusted">TRUSTED BY</h3>
  <div class="logo-row row-t1"><span class="logo logo--lumera">LUMERA</span><span class="logo logo--veroa"><span class="logo__dot"></span>VEROA</span><span class="logo logo--fenwick">Fenwick</span></div>
  <div class="logo-row row-t2"><span class="logo logo--harbour"><span class="logo__square"></span>Harbourgate<br>Port</span><span class="logo logo--alder"><span class="logo__dot"></span>ALDER</span></div>
</section>

<section class="banner banner--fade">
  <div class="brand"><span class="brand__mark"></span><span class="brand__name">COPPERLINE<br>VENTURES</span></div>
  <p class="tagline">YOUR TRUSTED PARTNER<br>IN DATA-DRIVEN DECISIONS</p>
  <ul class="benefits">
    <li>Unified data, analytics &amp; AI</li>
    <li>Trusted insights, faster outcomes</li>
    <li>Real-time intelligence at scale</li>
    <li>Enterprise-ready, secure solutions</li>
    <li>Clarity from data complexity</li>
  </ul>
  <h3 class="section-title title-partners">PARTNER WITH</h3>
  <div class="logo-row row-p1"><span class="logo logo--halvern"><span class="logo__square"></span>Halvern</span><span class="logo logo--tarnix">TARNIX</span></div>
  <div class="logo-row row-p2"><span class="logo logo--quillsoft"><span class="logo__dot"></span>quillsoft</span><span class="logo logo--meridex">meridex</span></div>
  <h3 class="section-title title-trusted">TRUSTED BY</h3>
  <div class="logo-row row-t1"><span class="logo logo--lumera">LUMERA</span><span class="logo logo--veroa"><span class="logo__dot"></span>VEROA</span><span class="logo logo--fenwick">Fenwick</span></div>
  <div class="logo-row row-t2"><span class="logo logo--harbour"><span class="logo__square"></span>Harbourgate<br>Port</span><span class="logo logo--alder"><span class="logo__dot"></span>ALDER</span></div>
</section>

</body>
</html>
```